Silverleaf Rise Accounting Program

size of ad Full: 7” x 9.6”
1- this is for a ladies program so it should appeal to women.
2-however, I do not want any pictures of people in this ad.
3-all the text should be seen and not covered over by graphics.
4-It should be an ad that will draw people's attention and people should look at it and say it looks nice I want to see that ad.
5-I have put all the instructions in yellow in the file below.
6-please leave 1 inch for the footer .
good luck with this project

• no picture or vector of people.

```html
<!DOCTYPE html>
<html lang="en">
<head>
<meta charset="utf-8">
<title>Silverleaf Rise Accounting Program – Master's Degree in Accounting</title>
<link rel="stylesheet" href="https://fonts.googleapis.com/css2?family=Oswald:wght@400;500;600&family=Roboto:wght@500;700&family=Roboto+Condensed:wght@700&display=swap">
<style>
  :root {
    --orange: #e9791c;
    --orange-deep: #e3711a;
    --slate-top: #344450;
    --slate-bottom: #1d2831;
    --ink: #1b1b1b;
    --white: #ffffff;
    --paper: #ffffff;
  }
  * { margin: 0; padding: 0; box-sizing: border-box; }
  html, body { width: 875px; height: 1200px; overflow: hidden; background: var(--paper); }
  .ad {
    position: relative;
    width: 875px;
    height: 1200px;
    overflow: hidden;
    background: var(--paper);
    font-family: "Oswald", sans-serif;
  }
  .top-strip {
    position: absolute; left: 0; top: 0; width: 875px; height: 52px;
    background: var(--orange);
    color: var(--white);
    font-family: "Roboto", sans-serif;
    font-weight: 500;
    font-size: 25px;
    letter-spacing: 22px;
    text-align: center;
    line-height: 52px;
    padding-left: 22px;
  }
  .hero {
    position: absolute; left: 0; top: 52px; width: 875px; height: 778px;
    background: linear-gradient(to bottom, var(--slate-top), var(--slate-bottom));
    text-align: center;
  }
  .headline {
    position: absolute; left: 0; top: 44px; width: 100%;
    color: var(--white);
    font-family: "Oswald", sans-serif;
    font-weight: 600;
    font-size: 132px;
    line-height: 117px;
    letter-spacing: 1px;
  }
  .benefits {
    position: absolute; left: 0; top: 418px; width: 100%;
    color: var(--orange);
    font-family: "Oswald", sans-serif;
    font-weight: 500;
    font-size: 35px;
    line-height: 51px;
  }
  .placement-title {
    position: absolute; left: 0; top: 650px; width: 100%;
    color: var(--white);
    font-family: "Roboto", sans-serif;
    font-weight: 500;
    font-size: 29px;
    letter-spacing: 0.5px;
  }
  .placement-stats {
    position: absolute; left: 0; top: 695px; width: 100%;
    color: var(--orange);
    font-family: "Roboto Condensed", sans-serif;
    font-weight: 700;
    font-size: 22px;
  }
  .placement-note {
    position: absolute; left: 0; top: 732px; width: 100%;
    color: var(--white);
    font-family: "Roboto Condensed", sans-serif;
    font-weight: 700;
    font-size: 18px;
  }
  .duration-burst {
    position: absolute; left: 684px; top: 759px; width: 160px; height: 160px;
  }
  .duration-burst text { font-family: "Oswald", sans-serif; fill: var(--white); text-anchor: middle; }
  .open-house {
    position: absolute; left: 37px; top: 854px;
    color: var(--ink);
    font-family: "Oswald", sans-serif;
    font-weight: 500;
    font-size: 31px;
    line-height: 42px;
  }
  .open-house .indent { padding-left: 8px; }
  .ranking-badge { position: absolute; left: 480px; top: 900px; width: 90px; height: 120px; }
  .rating-note {
    position: absolute; left: 578px; top: 934px; width: 295px;
    color: var(--ink);
    font-family: "Roboto Condensed", sans-serif;
    font-weight: 700;
    font-size: 20px;
    line-height: 23px;
    letter-spacing: 0.6px;
  }
  .contact-bar {
    position: absolute; left: 0; top: 1030px; width: 875px; height: 40px;
    background: var(--slate-bottom);
    color: var(--white);
    font-family: "Roboto", sans-serif;
    font-weight: 500;
    font-size: 19px;
    letter-spacing: 2.5px;
    line-height: 40px;
    text-align: center;
  }
  .contact-bar .or { color: var(--orange); }
</style>
</head>
<body>
<main class="ad">
  <header class="top-strip">ATTENTION WOMEN</header>

  <section class="hero">
    <h1 class="headline">A Master's<br>Degree in<br>Accounting</h1>
    <p class="benefits">A stable, lucrative career,<br>with high-paying,<br>full /part time opportunities<br>in Private/Public companies</p>
    <h2 class="placement-title">The Brightpath Job Placement advantage</h2>
    <p class="placement-stats">96% Placement Rate &nbsp;- &nbsp;6 placement directors &nbsp;- &nbsp;decades of relationships with 100's of firms</p>
    <p class="placement-note">Graduates have been placed in top companies (full/part time jobs).</p>
  </section>

  <svg class="duration-burst" viewBox="0 0 160 160" aria-label="Masters in 12 months">
    <polygon fill="var(--orange-deep)" points="155,80 141.8,92.3 149.3,108.7 132.4,115 133,133 115,132.4 108.7,149.3 92.3,141.8 80,155 67.7,141.8 51.3,149.3 45,132.4 27,133 27.6,115 10.7,108.7 18.2,92.3 5,80 18.2,67.7 10.7,51.3 27.6,45 27,27 45,27.6 51.3,10.7 67.7,18.2 80,5 92.3,18.2 108.7,10.7 115,27.6 133,27 132.4,45 149.3,51.3 141.8,67.7"/>
    <text x="80" y="56" font-size="17" font-weight="500">Masters in</text>
    <text x="80" y="105" font-size="50" font-weight="500">12</text>
    <text x="80" y="126" font-size="16" font-weight="500">months</text>
  </svg>

  <section class="open-house">
    <p>Meetwell open house</p>
    <p class="indent">Sunday, June 14, 2pm</p>
    <p>for a Meetwell link /</p>
    <p>conference number / information</p>
  </section>

  <svg class="ranking-badge" viewBox="0 0 90 120" role="img" aria-label="Program ranking badge">
    <circle cx="45" cy="48" r="40" fill="var(--orange)"/>
  </svg>

  <p class="rating-note">Hollowbrook University,<br>Masters in Accounting program,<br>received the highest possible<br>rating in USA</p>

  <footer class="contact-bar">nj@nj.brightpathjobs.org <span class="or">or</span> 732 555 0140 x 111</footer>
</main>
</body>
</html>
```